KPT Building And Maintenance

Need a very professional looking double sided Buisiness card with all my details phone number, name, email, license number.

Target Market(s)

construction industry

Industry/Entity Type

building

Contact Information for Business Card

Name Dale Whitcombe. Email Address Info@KPTBuilding.example.au mobile number 0452918730 licence number 871406D. web site

```html
<!DOCTYPE html>
<html lang="en">
<head>
<meta charset="utf-8">
<title>KPT Building And Maintenance – Business Card</title>
<link rel="stylesheet" href="https://fonts.googleapis.com/css2?family=Open+Sans:wght@400;600&family=Roboto+Condensed:wght@400;700&display=swap">
<style>
  :root {
    --backdrop: #e6e7e8;
    --card: #262729;
    --blue: #139fdc;
    --grey-band: #a7a8aa;
    --white: #f4f5f6;
    --text: #e9eaeb;
  }
  * { box-sizing: border-box; margin: 0; padding: 0; }
  html, body {
    width: 1200px; height: 1200px; overflow: hidden;
    background: var(--backdrop);
  }
  .card {
    position: absolute;
    left: 222px;
    width: 755px;
    height: 462px;
    background: var(--card);
    overflow: hidden;
  }
  .card--front { top: 105px; }
  .card--back { top: 630px; }

  .card__wave { position: absolute; left: 0; top: 0; width: 755px; height: 462px; }

  .brand {
    position: absolute;
    display: flex;
    align-items: center;
    font-family: "Open Sans", sans-serif;
    font-weight: 600;
    color: var(--white);
    text-transform: uppercase;
    letter-spacing: 1px;
  }
  .brand__mark { background: var(--blue); flex: none; }
  .card--front .brand { left: 48px; top: 196px; gap: 14px; font-size: 19px; line-height: 1.15; }
  .card--front .brand__mark { width: 44px; height: 44px; }
  .card--back .brand { left: 0; right: 0; top: 200px; justify-content: center; gap: 20px; font-size: 30px; line-height: 1.1; }
  .card--back .brand__mark { width: 66px; height: 66px; }

  .divider {
    position: absolute;
    left: 412px; top: 119px;
    width: 2px; height: 226px;
    background: var(--blue);
  }
  .details {
    position: absolute;
    left: 443px; top: 112px;
    font-family: "Open Sans", sans-serif;
    color: var(--text);
  }
  .details__name {
    font-family: "Roboto Condensed", sans-serif;
    font-weight: 700;
    font-size: 37px;
    line-height: 1.1;
    color: var(--blue);
  }
  .details__role {
    font-family: "Roboto Condensed", sans-serif;
    font-size: 23px;
    line-height: 1.2;
  }
  .details__licence { margin-top: 22px; font-size: 19px; }
  .details__licence span { color: var(--blue); }
  .contact { list-style: none; margin-top: 24px; font-size: 19px; }
  .contact li { display: flex; align-items: center; gap: 11px; height: 32px; }
  .contact svg { width: 20px; height: 20px; flex: none; }
</style>
</head>
<body>

<section class="card card--front">
  <svg class="card__wave" viewBox="0 0 755 462" aria-hidden="true">
    <path d="M0 362 Q360 520 755 378 L755 462 L0 462 Z" fill="var(--card)"/>
    <path d="M230 426 Q500 458 755 378 L755 398 Q500 472 230 426 Z" fill="var(--grey-band)"/>
    <path d="M0 362 Q330 490 755 403 L755 462 L0 462 Z" fill="var(--blue)"/>
  </svg>

  <div class="brand">
    <span class="brand__mark"></span>
    <span>KPT Building<br>And Maintenance</span>
  </div>

  <div class="divider"></div>

  <div class="details">
    <h1 class="details__name">Dale Whitcombe</h1>
    <p class="details__role">Owner</p>
    <p class="details__licence">licence number <span>871406D</span></p>
    <ul class="contact">
      <li>
        <svg viewBox="0 0 24 24"><path fill="var(--blue)" d="M6.6 10.8a15.1 15.1 0 0 0 6.6 6.6l2.2-2.2c.3-.3.7-.4 1-.2 1.1.4 2.3.6 3.6.6.6 0 1 .4 1 1V20c0 .6-.4 1-1 1A17 17 0 0 1 3 4c0-.6.4-1 1-1h3.5c.6 0 1 .4 1 1 0 1.3.2 2.5.6 3.6.1.3 0 .7-.2 1z"/></svg>
        0452918730
      </li>
      <li>
        <svg viewBox="0 0 24 24"><rect x="2" y="5" width="18" height="13" rx="1.5" fill="var(--blue)"/><path d="M3 6l8 6 8-6" stroke="var(--card)" stroke-width="1.6" fill="none"/><circle cx="19" cy="18" r="4.5" fill="var(--blue)" stroke="var(--card)" stroke-width="1.2"/><path d="M17 18l1.4 1.4 2.6-2.6" stroke="var(--white)" stroke-width="1.3" fill="none"/></svg>
        Info@KPTBuilding.example.au
      </li>
      <li>
        <svg viewBox="0 0 24 24" fill="none" stroke="var(--blue)" stroke-width="1.6"><circle cx="12" cy="12" r="9.5"/><ellipse cx="12" cy="12" rx="4.2" ry="9.5"/><path d="M2.5 12h19M4 7h16M4 17h16"/></svg>
        www.KPTBuilding.example
      </li>
    </ul>
  </div>
</section>

<section class="card card--back">
  <div class="brand">
    <span class="brand__mark"></span>
    <span>KPT Building<br>And Maintenance</span>
  </div>
</section>

</body>
</html>
```